A website for a Maltese Law Firm

Our law firm needs a website to further its business. The site should have a simple yet effective design. We would need the following sections: About us, Practice Areas, About Malta, Contact. These should be further split as follows:

About us: Our firm, Our values, What others say, Offices

Practice Areas: Crimimal, Citizenship & Residence, Overseas Patron Scheme, Criminal Defence, Civil Litigation, Arbitration and ADR, Commercial and Corporate, Media Law.

About Malta: just one section.

Contact: Just one section

We would also need a news feed at the front of the site to include latest news regarding our cases.

At the bottom we need a section for our Terms and a Privacy Statement.

Our logo is being attached.

Target Market(s)

All clients looking for legal assistance in Malta

Industry/Entity Type

Legal

Coding

Coded - Design and coding required

Number of Pages Required

1 page

Requirements
Must have
• It must be simple yet striking.

```html
<!DOCTYPE html>
<html lang="en">
<head>
<meta charset="utf-8">
<title>Calleira &amp; Vantoni Advocates</title>
<link rel="stylesheet" href="https://fonts.googleapis.com/css2?family=Raleway:wght@400;500;600;700;800&display=swap">
<style>
:root{
  --ink:#222;
  --text:#666;
  --muted:#888;
  --topbar:#eeeeee;
  --panel:#f2f2f2;
  --line:#555;
  --dark:#3b3b3b;
  --darker:#2c2c2c;
  --white:#fff;
  --practice:#2f2c2b;
}
*{box-sizing:border-box;margin:0;padding:0}
html,body{width:1200px;height:2198px;overflow:hidden}
body{font-family:'Raleway',sans-serif;color:var(--text);background:var(--white);position:relative}
.wrap{position:absolute;left:75px;right:75px}
section,header,footer,.topbar{position:absolute;left:0;width:1200px}

.topbar{top:0;height:54px;background:var(--topbar)}
.follow{position:absolute;left:0;top:14px;display:flex;align-items:center;gap:6px;font-size:10px;font-weight:700;color:#555;letter-spacing:.5px}
.follow .soc{width:27px;height:27px;border-radius:50%;background:#8a8a8a;display:inline-block}
.follow span.label{margin-right:8px}
.contact{position:absolute;right:0;top:18px;font-size:14px;color:#555;display:flex;align-items:center;gap:8px}
.contact b{font-weight:700;color:#444}
.contact svg{width:14px;height:14px;fill:#555}

header{top:54px;height:88px;background:var(--white)}
.brand{position:absolute;left:0;top:30px;display:flex;align-items:center;gap:10px;font-size:22px;font-weight:700;color:var(--ink);letter-spacing:.5px;text-transform:uppercase;line-height:28px}
.brand i{width:14px;height:14px;background:var(--ink);display:block}
nav.main{position:absolute;right:0;top:31px;display:flex;gap:0}
nav.main a{font-size:13px;font-weight:500;color:#444;text-decoration:none;padding:6px 19px;letter-spacing:.3px}
nav.main a.active{border-top:1px solid #333;border-bottom:1px solid #333;font-weight:700;color:#222}

.hero{top:142px;height:512px}
.hero-photo{position:absolute;inset:0;background:linear-gradient(180deg,#5b6f88 0%,#8f8fa0 22%,#c9a27a 38%,#55627a 55%,#2f4256 75%,#3d3a3f 100%)}
.hero-text{position:absolute;left:0;right:0;top:148px;text-align:center;color:var(--white)}
.hero-text h1{font-size:62px;font-weight:800;letter-spacing:1px;line-height:1}
.hero-text h2{font-size:44px;font-weight:800;letter-spacing:1px;margin-top:6px;line-height:1}
.hero-text p{font-size:31px;font-weight:500;margin-top:18px}
.btn-light{display:inline-block;margin-top:24px;color:#fff;font-size:15px;font-weight:700;border-top:1px solid #fff;border-bottom:1px solid #fff;padding:6px 56px}
.dots{position:absolute;left:0;right:0;top:474px;display:flex;justify-content:center;gap:9px}
.dots i{width:10px;height:10px;border-radius:50%;background:#fff;display:block}
.dots i.ring{background:transparent;border:2px solid #fff}

.intro{top:654px;height:492px}
.col{position:absolute;top:48px;width:330px}
.col h3,.news h3,.malta h3{font-size:23px;font-weight:700;color:var(--ink);letter-spacing:.3px}
.ph{width:330px;height:180px;margin-top:20px}
.col p{font-size:15px;line-height:26px;margin-top:20px;color:var(--text)}
.btn{display:inline-block;font-size:13px;font-weight:700;color:#444;border-top:1px solid var(--line);border-bottom:1px solid var(--line);padding:7px 14px}
.col .btn{margin-top:20px}
.news{position:absolute;left:718px;top:49px;width:332px;height:394px;background:var(--panel);padding:22px 27px}
.news ul{list-style:none;margin-top:8px}
.news li{padding:13px 0 10px;border-bottom:1px solid #ddd}
.news li:last-child{border-bottom:0}
.news time{font-size:14px;font-weight:700;color:#444;display:block}
.news li p{font-size:14px;line-height:26px;margin-top:4px}
.news .btn{position:absolute;right:18px;bottom:18px}

.practice{top:1146px;height:403px;background:var(--practice);color:var(--white)}
.practice-bg{position:absolute;inset:0;background:linear-gradient(90deg,#2a2726 0%,#4a4543 50%,#2a2726 100%);opacity:.9}
.practice h3{position:absolute;top:42px;left:0;right:0;text-align:center;font-size:23px;font-weight:600;letter-spacing:.5px}
.area{position:absolute;top:103px;width:250px;text-align:center}
.area .icon{width:100px;height:100px;border-radius:50%;background:#111;border:2px solid #555;margin:0 auto;display:flex;align-items:center;justify-content:center}
.area .icon svg{width:32px;height:32px;fill:#fff}
.area h4{font-size:16px;font-weight:700;margin-top:24px;line-height:22px;letter-spacing:.2px}
.area p{font-size:15px;line-height:23px;margin:10px auto 0;width:190px;color:#ddd}
.arrow{position:absolute;top:188px;width:20px;height:24px}
.arrow svg{width:20px;height:24px;fill:none;stroke:#fff;stroke-width:4}

.malta{top:1549px;height:389px}
.malta .ph{position:absolute;left:0;top:49px;width:511px;height:276px;margin:0}
.malta .copy{position:absolute;left:555px;top:64px;width:495px}
.malta .copy p{font-size:15px;line-height:26px;margin-top:17px}
.malta .copy .btn{margin-top:26px}

.footnav{top:1938px;height:70px;background:var(--topbar)}
.footnav nav{position:absolute;left:0;top:29px;font-size:11px;font-weight:700;color:#444;letter-spacing:.3px}
.footnav nav span{margin:0 14px;color:#777}
.footnav .follow{left:auto;right:0;top:21px}

.legal{top:2008px;height:140px;background:var(--dark);color:#bbb}
.legal .block{position:absolute;top:36px;width:500px}
.legal h5{font-size:13px;font-weight:700;color:#eee;letter-spacing:.3px}
.legal p{font-size:13px;line-height:21px;margin-top:6px;color:#aaa}
.copyright{top:2148px;height:50px;background:var(--darker);text-align:center;font-size:11px;color:#999;line-height:50px}
</style>
</head>
<body>

<div class="topbar">
  <div class="wrap">
    <div class="follow"><span class="label">FOLLOW US</span>
      <i class="soc" aria-label="Social link"></i><i class="soc" aria-label="Social link"></i><i class="soc" aria-label="Social link"></i><i class="soc" aria-label="Social link"></i><i class="soc" aria-label="Social link"></i>
    </div>
    <div class="contact">
      <svg viewBox="0 0 16 16"><rect x="0" y="0" width="16" height="16" rx="2"/><path d="M4 3l2 0 1 3-1.5 1a7 7 0 0 0 3.5 3.5L10 9l3 1v2a1 1 0 0 1-1 1C7 13 3 9 3 4a1 1 0 0 1 1-1z" fill="#eee"/></svg>
      <b>1-800-555-0147</b><span>&nbsp;|&nbsp;</span>
      <svg viewBox="0 0 16 16"><rect x="0" y="3" width="16" height="11" rx="1"/><path d="M0 4l8 5 8-5" stroke="#eee" stroke-width="1.3" fill="none"/></svg>
      <span>info@calleiravantoni.com</span>
    </div>
  </div>
</div>

<header>
  <div class="wrap">
    <div class="brand"><i></i>Calleira &amp; Vantoni Advocates</div>
    <nav class="main">
      <a class="active">HOME</a><a>ABOUT US</a><a>PRACTICE AREAS</a><a>ABOUT MALTA</a><a>CONTACT US</a>
    </nav>
  </div>
</header>

<section class="hero">
  <div class="hero-photo" role="img" aria-label="Evening view over a Maltese harbour bay with city lights"></div>
  <div class="hero-text">
    <h1>CALLEIRA &amp; VANTONI</h1>
    <h2>ADVOCATES</h2>
    <p>We are a law firm from Malta</p>
    <span class="btn-light">READ MORE</span>
  </div>
  <div class="dots"><i></i><i class="ring"></i><i></i><i></i></div>
</section>

<section class="intro">
  <div class="wrap">
    <div class="col" style="left:0">
      <h3>WELCOME !</h3>
      <div class="ph" role="img" aria-label="Lawyers in a meeting room" style="background:linear-gradient(135deg,#c9d3dc,#7d8894 60%,#3d444c)"></div>
      <p>Aliquam molestie, mi et imperdiet euismod, dui purus auctor tellus, et interdum lacus lectus et ante. Sed accumsan sollicitudin sapien, sit amet adipiscing...</p>
      <span class="btn">READ MORE</span>
    </div>
    <div class="col" style="left:359px">
      <h3>ABOUT US</h3>
      <div class="ph" role="img" aria-label="Two colleagues reviewing a document" style="background:linear-gradient(135deg,#b8a3b4,#d9c2b4 50%,#e8e4e6)"></div>
      <p>Aliquam molestie, mi et imperdiet euismod, dui purus auctor tellus, et interdum lacus lectus et ante. Sed accumsan sollicitudin sapien, sit amet adipiscing...</p>
      <span class="btn">READ MORE</span>
    </div>
    <aside class="news">
      <h3>LATEST NEWS</h3>
      <ul>
        <li><time>Jun 08, 2016</time><p>Aliquam molestie, mi et imperdiet euismod, dui purus auctor...</p></li>
        <li><time>Jun 08, 2016</time><p>Aliquam molestie, mi et imperdiet euismod, dui purus auctor...</p></li>
        <li><time>Jun 08, 2016</time><p>Aliquam molestie, mi et imperdiet euismod, dui purus auctor...</p></li>
      </ul>
      <span class="btn">READ MORE</span>
    </aside>
  </div>
</section>

<section class="practice">
  <div class="practice-bg" role="img" aria-label="Dim columned court hall"></div>
  <h3>PRACTICE AREAS</h3>
  <span class="arrow" style="left:43px"><svg viewBox="0 0 20 24"><path d="M14 3L5 12l9 9"/></svg></span>
  <span class="arrow" style="left:1139px"><svg viewBox="0 0 20 24"><path d="M6 3l9 9-9 9"/></svg></span>
  <div class="area" style="left:71px">
    <div class="icon"><svg viewBox="0 0 32 32"><circle cx="16" cy="10" r="6"/><path d="M5 28c0-7 5-10 11-10s11 3 11 10z"/></svg></div>
    <h4>CRIMIMAL</h4>
    <p>Aenean a nibh eget turpis vehicula tempus ac sed massa laoreet non..</p>
  </div>
  <div class="area" style="left:342px">
    <div class="icon"><svg viewBox="0 0 32 32"><path d="M16 4L2 16h4v12h8v-8h4v8h8V16h4z"/></svg></div>
    <h4>CITIZENSHIP &amp; RESIDENCE</h4>
    <p>Aenean a nibh eget turpis vehicula tempus ac sed massa laoreet non..</p>
  </div>
  <div class="area" style="left:612px">
    <div class="icon"><svg viewBox="0 0 32 32"><path d="M16 2L2 9v3h28V9z"/><rect x="5" y="13" width="3" height="11"/><rect x="11" y="13" width="3" height="11"/><rect x="18" y="13" width="3" height="11"/><rect x="24" y="13" width="3" height="11"/><rect x="2" y="25" width="28" height="4"/></svg></div>
    <h4>CIVIL LITIGATION</h4>
    <p>Aenean a nibh eget turpis vehicula tempus ac sed massa laoreet non..</p>
  </div>
  <div class="area" style="left:880px">
    <div class="icon"><svg viewBox="0 0 32 32"><path d="M6 2h14l7 7v21H6z"/><path d="M10 14h13M10 19h13M10 24h13" stroke="#111" stroke-width="2"/></svg></div>
    <h4>OVERSEAS PATRON<br>SCHEME</h4>
    <p>Aenean a nibh eget turpis vehicula tempus ac sed massa laoreet non..</p>
  </div>
</section>

<section class="malta">
  <div class="wrap">
    <div class="ph" role="img" aria-label="Valletta skyline at dusk above the sea" style="background:linear-gradient(180deg,#9fb6c8 0%,#c9b79a 35%,#b57a3e 65%,#5d4330 100%)"></div>
    <div class="copy">
      <h3>ABOUT MALTA</h3>
      <p>Aliquam molestie, mi et imperdiet euismod, dui purus auctor tellus, et interdum lacus lectus et ante. Sed accumsan sollicitudin sapien, sit amet adipiscing.. Duis aliquam nibh a dui iaculis viverra id a velit. Vivamus egestas risus in magna varius commodo. Sed semper viverra egestas. Etiam pretium porttitor lectus, vel ornare neque porta volutpat.</p>
      <span class="btn">READ MORE</span>
    </div>
  </div>
</section>

<footer class="footnav">
  <div class="wrap">
    <nav>HOME<span>/</span>ABOUT US<span>/</span>PRACTICE AREAS<span>/</span>ABOUT MALTA<span>/</span>CONTACT US</nav>
    <div class="follow"><span class="label">FOLLOW US</span>
      <i class="soc" aria-label="Social link"></i><i class="soc" aria-label="Social link"></i><i class="soc" aria-label="Social link"></i><i class="soc" aria-label="Social link"></i><i class="soc" aria-label="Social link"></i>
    </div>
  </div>
</footer>

<footer class="legal">
  <div class="wrap">
    <div class="block" style="left:0">
      <h5>TERMS &amp; CONDITIONS:</h5>
      <p>Duis aliquam nibh a dui iaculis viverra id a velit. Vivamus egestas risus in magna varius commodo. Sed semper viverra egestas. Etiam pretium porttitor lectus, vel ornare neque porta volutpat.</p>
    </div>
    <div class="block" style="left:539px">
      <h5>PRIVACY POLICY</h5>
      <p>Duis aliquam nibh a dui iaculis viverra id a velit. Vivamus egestas risus in magna varius commodo. Sed semper viverra egestas. Etiam pretium porttitor lectus, vel ornare neque porta volutpat.</p>
    </div>
  </div>
</footer>

<footer class="copyright">Copyright © 2016, Calleira &amp; Vantoni All Right Reserved</footer>

</body>
</html>
```